Feral Highland Pages
Feral Highland Pages - Outdoors
Creative Brief
Use specific fonts
Possibles are Birch, Oakwood, Eurostile or another outdoors themed abstract type
Professional
Derek Hollins
c/o Velloway Productions 4820 Copperfield Lane Bear Creek, PA 17455
dhollins@derekhollinsphoto.com
www.derekhollinsphoto.com
"Never take from nature.....just take what nature gives you"!
I want this to be as professional as possible but still relate to nature.

```html
<!DOCTYPE html>
<html lang="en">
<head>
<meta charset="utf-8">
<title>Feral Highland Pages – Stationery Set</title>
<link rel="stylesheet" href="https://fonts.googleapis.com/css2?family=Oswald:wght@400;700&display=swap">
<style>
  :root {
    --board: #3a3a3a;
    --board-light: #4a4a4a;
    --paper: #f7f7f7;
    --paper-shade: #e6e6e6;
    --ink: #161616;
    --band: #1c1c1c;
    --muted: #9a9a9a;
    --caption: #bdbdbd;
    --watermark: #ececec;
  }
  * { margin: 0; padding: 0; box-sizing: border-box; }
  html, body { width: 1200px; height: 350px; overflow: hidden; }
  body {
    background: radial-gradient(ellipse at 50% 40%, var(--board-light), var(--board));
    font-family: "Oswald", sans-serif;
    position: relative;
  }
  .piece {
    position: absolute;
    background: var(--paper);
    box-shadow: 0 2px 6px rgba(0,0,0,.45);
    overflow: hidden;
  }
  .piece--dark { background: var(--band); }
  .caption {
    position: absolute;
    font-size: 5px;
    color: var(--caption);
    letter-spacing: .3px;
    white-space: nowrap;
  }
  .brand {
    position: absolute;
    font-weight: 700;
    color: var(--ink);
    text-transform: uppercase;
    line-height: 1;
    display: flex;
    align-items: center;
    gap: 3px;
    white-space: nowrap;
  }
  .brand--light { color: var(--paper); }
  .brand__dot {
    display: inline-block;
    border-radius: 50%;
    background: currentColor;
  }
  .contact-band {
    position: absolute;
    top: 0; bottom: 0;
    background: var(--band);
    color: var(--paper);
  }
  .contact {
    position: absolute;
    font-weight: 400;
    line-height: 1.35;
    color: var(--muted);
    white-space: nowrap;
  }
  .contact--right { text-align: right; }
  .contact--light { color: var(--paper); }
  .watermark {
    position: absolute;
    border-radius: 50%;
    background: radial-gradient(circle, var(--watermark), transparent 70%);
  }
  .envelope__flap { position: absolute; left: 0; top: 0; }
</style>
</head>
<body>

<!-- Business cards -->
<div class="piece" style="left:24px;top:72px;width:125px;height:65px;">
  <div class="brand" style="left:14px;top:28px;font-size:8px;"><span class="brand__dot" style="width:6px;height:6px;"></span>Feral Highland Pages</div>
</div>
<div class="caption" style="left:24px;top:140px;">Business card back</div>

<div class="piece piece--dark" style="left:24px;top:154px;width:125px;height:69px;">
  <div class="brand brand--light" style="left:10px;top:14px;font-size:8px;"><span class="brand__dot" style="width:6px;height:6px;"></span>Feral Highland Pages</div>
  <div class="contact contact--light" style="left:10px;top:34px;font-size:4px;">
    Derek Hollins<br>c/o Velloway Productions<br>4820 Copperfield Lane, Bear Creek, PA 17455<br>dhollins@derekhollinsphoto.com<br>www.derekhollinsphoto.com
  </div>
</div>
<div class="caption" style="left:24px;top:226px;">Business card front</div>

<div class="piece" style="left:24px;top:242px;width:125px;height:65px;">
  <div class="brand" style="left:10px;top:12px;font-size:7px;"><span class="brand__dot" style="width:5px;height:5px;"></span>Feral Highland Pages</div>
  <div class="contact" style="left:10px;top:30px;font-size:4px;">
    Derek Hollins<br>dhollins@derekhollinsphoto.com<br>www.derekhollinsphoto.com
  </div>
</div>
<div class="caption" style="left:24px;top:310px;">Business card alt</div>

<!-- Letterheads -->
<div class="piece" style="left:230px;top:19px;width:159px;height:298px;">
  <div class="contact contact--right" style="right:20px;top:8px;font-size:3.5px;">Derek Hollins<br>4820 Copperfield Lane<br>Bear Creek, PA 17455<br>www.derekhollinsphoto.com</div>
  <div class="brand" style="left:18px;top:34px;font-size:8px;"><span class="brand__dot" style="width:6px;height:6px;"></span>Feral Highland Pages</div>
  <div class="watermark" role="img" aria-label="Faint antlered deer silhouette decoration" style="left:20px;top:80px;width:110px;height:110px;"></div>
  <div class="contact-band" style="right:0;width:14px;top:0;height:60px;bottom:auto;"></div>
</div>
<div class="caption" style="left:230px;top:320px;">Letterhead first page</div>

<div class="piece" style="left:403px;top:19px;width:159px;height:298px;">
  <div class="contact contact--right" style="right:20px;top:8px;font-size:3.5px;">Derek Hollins<br>4820 Copperfield Lane<br>Bear Creek, PA 17455<br>www.derekhollinsphoto.com</div>
  <div class="brand" style="left:18px;top:34px;font-size:8px;"><span class="brand__dot" style="width:6px;height:6px;"></span>Feral Highland Pages</div>
  <div class="watermark" role="img" aria-label="Faint antlered deer silhouette decoration" style="left:20px;top:80px;width:110px;height:110px;"></div>
  <div class="contact-band" style="right:0;width:14px;top:150px;height:60px;bottom:auto;"></div>
</div>
<div class="caption" style="left:403px;top:320px;">Letterhead second page</div>

<!-- Compliment cards and slips -->
<div class="piece" style="left:643px;top:96px;width:77px;height:53px;">
  <div class="brand" style="left:5px;top:22px;font-size:4.5px;"><span class="brand__dot" style="width:3.5px;height:3.5px;"></span>Feral Highland Pages</div>
  <div class="contact-band" style="right:0;width:8px;"></div>
</div>
<div class="caption" style="left:643px;top:151px;">Compliment card</div>

<div class="piece" style="left:739px;top:34px;width:58px;height:48px;">
  <div class="brand" style="left:4px;top:8px;font-size:4px;"><span class="brand__dot" style="width:3px;height:3px;"></span>Feral Highland Pages</div>
  <div class="contact" style="left:4px;top:20px;font-size:3px;">Derek Hollins<br>www.derekhollinsphoto.com</div>
</div>
<div class="caption" style="left:739px;top:85px;">Note card</div>

<div class="piece" style="left:643px;top:164px;width:144px;height:42px;">
  <div class="brand" style="left:10px;top:10px;font-size:6px;"><span class="brand__dot" style="width:4px;height:4px;"></span>Feral Highland Pages</div>
  <div class="contact" style="left:10px;top:22px;font-size:3.5px;">dhollins@derekhollinsphoto.com · www.derekhollinsphoto.com</div>
  <div class="contact-band" style="right:0;width:8px;"></div>
</div>
<div class="caption" style="left:643px;top:209px;">Compliment slip</div>

<div class="piece" style="left:643px;top:230px;width:211px;height:84px;">
  <div class="contact" style="left:12px;top:10px;font-size:3.5px;">Derek Hollins · c/o Velloway Productions · 4820 Copperfield Lane, Bear Creek, PA 17455</div>
  <div class="brand" style="left:40px;top:40px;font-size:10px;"><span class="brand__dot" style="width:7px;height:7px;"></span>Feral Highland Pages</div>
  <div class="contact-band" style="right:0;width:10px;"></div>
</div>
<div class="caption" style="left:643px;top:317px;">Comp slip long</div>

<!-- Envelopes -->
<div class="piece" style="left:870px;top:34px;width:258px;height:91px;">
  <svg class="envelope__flap" width="258" height="40" viewBox="0 0 258 40" aria-hidden="true">
    <path d="M0 0 H258 V12 L129 40 L0 12 Z" fill="var(--band)"/>
  </svg>
  <div class="brand brand--light" style="left:96px;top:10px;font-size:6px;"><span class="brand__dot" style="width:4px;height:4px;"></span>Feral Highland Pages</div>
</div>
<div class="caption" style="left:870px;top:128px;">Envelope open</div>

<div class="piece" style="left:870px;top:139px;width:258px;height:82px;">
  <svg class="envelope__flap" width="258" height="82" viewBox="0 0 258 82" aria-hidden="true">
    <path d="M0 0 L129 42 L258 0" fill="none" stroke="var(--paper-shade)" stroke-width="1.5"/>
    <path d="M0 82 L110 36 M258 82 L148 36" stroke="var(--paper-shade)" stroke-width="1"/>
  </svg>
  <div class="brand" style="left:98px;top:50px;font-size:6px;"><span class="brand__dot" style="width:4px;height:4px;"></span>Feral Highland Pages</div>
</div>
<div class="caption" style="left:870px;top:224px;">Envelope back</div>

<div class="piece" style="left:870px;top:230px;width:258px;height:82px;">
  <div class="brand" style="left:12px;top:10px;font-size:6px;"><span class="brand__dot" style="width:4px;height:4px;"></span>Feral Highland Pages</div>
  <div class="contact" style="left:12px;top:20px;font-size:3.5px;">4820 Copperfield Lane<br>Bear Creek, PA 17455</div>
</div>
<div class="caption" style="left:870px;top:315px;">Envelope front</div>

</body>
</html>
```